Harborview Wellness Counseling
7 business cards, letterhead, envlp, fax cover
Harborview Wellness Counseling -
Creative Brief
Professional
Martin Oakridge
Owner/Manager
2875 Pellham Ridge Blvd. Suite 204 Cedarbrook, WA 63412
oakridgehome@brisknet-mail.net
I need cards for each of my seven therapists. I will upload word file with their names and info. Letterhead should not use therapists names.

```html
<!DOCTYPE html>
<html lang="en">
<head>
<meta charset="utf-8">
<title>Harborview Wellness Counseling – Stationery Set</title>
<link href="https://fonts.googleapis.com/css2?family=Libre+Baskerville:wght@400;700&display=swap" rel="stylesheet">
<style>
  :root {
    --navy: #1d3c6e;
    --orange: #f2a21b;
    --green: #6cb33f;
    --red: #e4572e;
    --ink: #33415c;
    --paper: #ffffff;
    --frame: #cfd3d8;
    --shadow: rgba(0, 0, 0, 0.22);
    --watermark: #dfe6ef;
    --fold: #9aa2ad;
  }
  * { box-sizing: border-box; margin: 0; padding: 0; }
  html, body { width: 1200px; height: 741px; overflow: hidden; background: var(--paper); }
  body { font-family: "Libre Baskerville", Georgia, serif; color: var(--ink); position: relative; }

  .stage-frame {
    position: absolute; left: 22px; top: 22px; width: 1156px; height: 697px;
    border: 1px solid var(--frame);
  }
  .sheet {
    position: absolute; background: var(--paper);
    box-shadow: 2px 3px 6px var(--shadow);
  }
  .color-bar { display: flex; height: 8px; width: 100%; }
  .color-bar span { flex: 1; }
  .color-bar .navy { background: var(--navy); }
  .color-bar .orange { background: var(--orange); }
  .color-bar .green { background: var(--green); }
  .color-bar .red { background: var(--red); }

  .brand { display: flex; align-items: center; gap: 5px; }
  .brand-dot { width: 12px; height: 12px; border-radius: 50%; background: var(--orange); flex: none; }
  .brand-name {
    font-weight: 700; color: var(--navy); text-transform: uppercase;
    font-size: 8px; white-space: nowrap;
  }
  .brand-tag { font-size: 5px; color: var(--ink); margin-top: 2px; white-space: nowrap; }

  /* Envelope front */
  .envelope-front { left: 60px; top: 156px; width: 497px; height: 192px; }
  .envelope-front .brand-block { position: absolute; left: 22px; top: 22px; }
  .envelope-front .brand-tag { margin-left: 17px; }
  .envelope-front .return-address {
    position: absolute; left: 34px; top: 70px; font-size: 6.5px; line-height: 1.5;
    font-style: normal; text-align: center;
  }

  /* Envelope back */
  .envelope-back { left: 60px; top: 444px; width: 497px; height: 204px; }
  .envelope-back svg { position: absolute; inset: 0; }
  .envelope-back .flap-seal {
    position: absolute; left: 50%; top: 38px; transform: translateX(-50%);
  }

  /* Letterhead */
  .letterhead { left: 631px; top: 89px; width: 406px; height: 571px; }
  .letterhead .brand-block { position: absolute; left: 100px; top: 22px; }
  .letterhead .brand-name { font-size: 9px; }
  .letterhead .brand-tag { margin-left: 17px; text-align: center; }
  .letterhead .watermark {
    position: absolute; left: 113px; top: 176px; width: 176px; height: 176px; border-radius: 50%;
    background: radial-gradient(circle, var(--watermark) 0%, #eef2f7 60%, rgba(255,255,255,0) 72%);
  }
  .letterhead .footer {
    position: absolute; left: 0; right: 0; bottom: 18px; text-align: center;
    font-size: 6px; white-space: nowrap;
  }

  /* Business card */
  .business-card { left: 967px; top: 305px; width: 190px; height: 117px; }
  .business-card .brand-block { position: absolute; left: 10px; top: 12px; }
  .business-card .brand-dot { width: 8px; height: 8px; }
  .business-card .brand-name { font-size: 5.5px; }
  .business-card .brand-tag { font-size: 4px; margin-left: 13px; }
  .business-card .person { position: absolute; left: 0; right: 0; top: 50px; text-align: center; }
  .business-card .person-name { font-size: 6.5px; font-weight: 700; color: var(--navy); }
  .business-card .person-title { font-size: 5px; margin-top: 2px; }
  .business-card .card-contact {
    position: absolute; left: 0; right: 0; bottom: 12px; text-align: center;
    font-size: 4.4px; line-height: 1.6; white-space: nowrap;
  }
</style>
</head>
<body>
  <div class="stage-frame"></div>

  <section class="sheet envelope-front">
    <div class="color-bar"><span class="navy"></span><span class="orange"></span><span class="green"></span><span class="red"></span></div>
    <div class="brand-block">
      <div class="brand"><span class="brand-dot"></span><span class="brand-name">Harborview Wellness Counseling</span></div>
      <div class="brand-tag">Marriage &amp; Family Therapy, LLC</div>
    </div>
    <address class="return-address">
      2875 Pellham Ridge Blvd., Suite 204<br>Cedarbrook, WA 63412
    </address>
  </section>

  <section class="sheet envelope-back">
    <svg width="497" height="204" viewBox="0 0 497 204">
      <path d="M0 0 Q 20 50 200 70 Q 248 76 296 70 Q 477 50 497 0" fill="none" stroke="var(--fold)" stroke-width="1" stroke-dasharray="3 2"/>
    </svg>
    <div class="flap-seal brand"><span class="brand-dot"></span></div>
  </section>

  <section class="sheet letterhead">
    <div class="color-bar"><span class="navy"></span><span class="orange"></span><span class="green"></span><span class="red"></span></div>
    <div class="brand-block">
      <div class="brand"><span class="brand-dot"></span><span class="brand-name">Harborview Wellness Counseling</span></div>
      <div class="brand-tag">Marriage &amp; Family Therapy, LLC</div>
    </div>
    <div class="watermark" role="img" aria-label="Faint decorative emblem area"></div>
    <div class="footer">2875 Pellham Ridge Blvd., Suite 204, Cedarbrook, WA 63412 &nbsp;|&nbsp; Phone: 555-201-0142 &nbsp;|&nbsp; Fax: 555-201-0143</div>
  </section>

  <section class="sheet business-card">
    <div class="color-bar" style="height:5px"><span class="navy"></span><span class="orange"></span><span class="green"></span><span class="red"></span></div>
    <div class="brand-block">
      <div class="brand"><span class="brand-dot"></span><span class="brand-name">Harborview Wellness Counseling</span></div>
      <div class="brand-tag">Marriage &amp; Family Therapy, LLC</div>
    </div>
    <div class="person">
      <div class="person-name">Martin Oakridge</div>
      <div class="person-title">Owner/Manager</div>
    </div>
    <div class="card-contact">
      2875 Pellham Ridge Blvd., Suite 204, Cedarbrook, WA 63412<br>
      555-201-0148 &nbsp;|&nbsp; oakridgehome@brisknet-mail.net
    </div>
  </section>
</body>
</html>
```